Grand Opening / Live Music Event

My band is playing a Grand Opening event on Saturday April 5th. I need a flyer utilizing the attached image of our bass player and incorporating our band logo. This picture makes me laugh and gives the impression he is angry - like saying "it's going to be a celebration fool!" or something along those lines. I need to the flyer to pop and present an image that it will be an excellent party. Feel free to incorporate any background or theme style. You can find other images of my band in the event they are needed at: https://www.velorumhub.example/Corkvalleyband

Some details:

The event will be at Quimby's Hall. 8241 Larkspur Ave. #204, Frisco, Texas. (214) 705-9183 for table reservations.

Saturday April 5th. Party starts at 7:00 PM with an acoustic set by the Velvet Otters and Cork Valley taking the stage at 10:00 PM.

Hottest new bar in Frisco! Drink specials all night with the Zephyr Pale girls, and great live music to celebrate this grand opening.

I will use this for FB and other online marketing, as well as some print.

```html
<!DOCTYPE html>
<html lang="en">
<head>
<meta charset="utf-8">
<title>Grand Opening – Quimby's Hall</title>
<link rel="stylesheet" href="https://fonts.googleapis.com/css2?family=Londrina+Solid:wght@400;900&family=Montserrat:wght@500;700&family=Questrial&display=swap">
<style>
  :root {
    --ink: #141414;
    --white: #ffffff;
    --mauve: #c8a3c6;
    --grey-pink: #b9aab3;
    --rust: #d8763c;
    --brown: #8a5a3e;
    --crimson: #b23446;
    --stage-blue: #1f3f9a;
    --stage-navy: #0d1c55;
    --stage-red: #9c2c4a;
    --sky: #8fd8e8;
    --blush: #e7b3c8;
    --time-blue: #3c78c6;
    --ready-red: #b7363f;
    --ready-grey: #d8d1d3;
    --mint: #47c29c;
    --lavender: #8d80d2;
  }
  * { box-sizing: border-box; margin: 0; padding: 0; }
  html, body { width: 849px; height: 1200px; overflow: hidden; background: var(--mauve); }

  .flyer {
    position: relative;
    width: 849px;
    height: 1200px;
    overflow: hidden;
    background: linear-gradient(180deg, var(--grey-pink) 0%, var(--mauve) 40%, #d59bbf 100%);
  }

  .headline {
    position: absolute;
    left: 0; top: 0;
    width: 849px; height: 190px;
    background: linear-gradient(90deg, #9f9aa0, #d8b9cc 50%, #a7a1a6);
  }
  .headline h1 {
    position: absolute;
    left: 0; top: 10px; width: 849px;
    text-align: center;
    font-family: "Londrina Solid", sans-serif;
    font-weight: 900;
    font-size: 116px;
    line-height: 1;
    letter-spacing: 14px;
    color: var(--ink);
  }

  .side-pattern {
    position: absolute;
    left: 0; top: 197px;
    width: 121px; height: 430px;
    background: linear-gradient(180deg, var(--rust) 0%, #c99458 45%, var(--brown) 100%);
  }

  .venue-band {
    position: absolute;
    left: 121px; top: 197px;
    width: 712px; height: 95px;
    background: var(--crimson);
  }
  .venue-band h2 {
    font-family: "Montserrat", sans-serif;
    font-weight: 700;
    font-size: 66px;
    letter-spacing: 6px;
    line-height: 95px;
    text-align: center;
    color: var(--white);
  }

  .band-photo {
    position: absolute;
    left: 121px; top: 292px;
    width: 577px; height: 335px;
    background: radial-gradient(ellipse at 45% 55%, var(--stage-red) 0%, var(--stage-blue) 45%, var(--stage-navy) 100%);
  }

  .date-column {
    position: absolute;
    left: 698px; top: 292px;
    width: 135px; height: 335px;
    background: linear-gradient(180deg, #e0744a 0%, #d6548a 55%, #b86a4c 100%);
    color: var(--white);
    font-family: "Montserrat", sans-serif;
    font-weight: 500;
    text-align: center;
  }
  .date-column .month,
  .date-column .day { position: absolute; left: 0; right: 0; display: block; }
  .date-column .month { top: 88px; font-size: 30px; letter-spacing: 2px; }
  .date-column .day { top: 130px; font-size: 56px; }
  .date-column .day sup { font-size: 32px; vertical-align: 22px; }

  .band-mark {
    position: absolute;
    left: 7px; top: 634px;
    width: 556px; height: 349px;
    background: linear-gradient(135deg, var(--blush), #cfb8d8);
    display: flex; align-items: center; justify-content: center; gap: 18px;
  }
  .band-mark .mark-square { width: 34px; height: 34px; background: var(--sky); }
  .band-mark .mark-name {
    font-family: "Montserrat", sans-serif;
    font-weight: 500;
    font-size: 46px;
    letter-spacing: 8px;
    color: var(--ink);
  }

  .headliner-time {
    position: absolute;
    left: 570px; top: 634px;
    width: 270px; height: 107px;
    background: var(--time-blue);
    font-family: "Montserrat", sans-serif;
    font-weight: 500;
    font-size: 60px;
    line-height: 107px;
    text-align: center;
    color: var(--white);
  }

  .ready {
    position: absolute;
    left: 577px; top: 748px;
    width: 263px; height: 235px;
    background: linear-gradient(90deg, var(--ready-red) 0 48%, #5a4e8e 48% 100%);
    font-family: "Londrina Solid", sans-serif;
    font-weight: 400;
    font-size: 62px;
    line-height: 1.15;
    color: var(--ready-grey);
    padding: 40px 0 0 40px;
  }

  .opener-band {
    position: absolute;
    left: 0; top: 994px;
    width: 849px; height: 114px;
    background: linear-gradient(90deg, var(--mint), #63c89a 60%, #3fb6a3);
    color: var(--white);
  }
  .opener-band .earlier {
    position: absolute; left: 4px; top: 62px;
    font-family: "Montserrat", sans-serif;
    font-weight: 500; font-size: 22px; letter-spacing: 1px;
  }
  .opener-band .opener {
    position: absolute; left: 134px; top: 16px;
    font-family: "Londrina Solid", sans-serif;
    font-weight: 400; font-size: 75px; letter-spacing: 2px; line-height: 1;
    white-space: nowrap;
  }

  .details {
    position: absolute;
    left: 0; top: 1114px;
    width: 849px; height: 86px;
    background: var(--lavender);
    font-family: "Questrial", sans-serif;
    font-size: 23px;
    line-height: 27px;
    color: var(--ink);
    padding: 18px 0 0 176px;
  }
</style>
</head>
<body>
<main class="flyer">
  <header class="headline"><h1>grand opening</h1></header>

  <div class="side-pattern" role="img" aria-label="Orange and brown retro dot pattern panel"></div>

  <section class="venue-band"><h2>QUIMBY'S HALL</h2></section>

  <div class="band-photo" role="img" aria-label="Photo of the bass player on stage under blue lights"></div>

  <div class="date-column">
    <span class="month">APRIL</span>
    <span class="day">5<sup>TH</sup></span>
  </div>

  <div class="band-mark">
    <span class="mark-square"></span>
    <span class="mark-name">CORK VALLEY</span>
  </div>

  <div class="headliner-time">10:00PM</div>

  <div class="ready">ARE U<br>READY ?</div>

  <section class="opener-band">
    <span class="earlier">EARLIER</span>
    <span class="opener">VELVET OTTERS 7:00PM</span>
  </section>

  <footer class="details">
    <p>8241 Larkspur Ave. #204, Frisco, Texas</p>
    <p>(214) 705-9183 for table reservations</p>
  </footer>
</main>
</body>
</html>
```